Sudden Tides "Lantern Road" New Single Cover

Create cover artwork for the band Sudden Tides' new single "Lantern Road" being released early 2020. Style, font and graphics to be consistent with band's previous releases and overall brand identity. Visit www.suddentidesband.example and our Spotify page https://music.example.net/artist/7QzWpLx3RtVnKd8e2YbHcJ?si=MUrTgKa4PLe7skvWq2AmZd to view our previous releases and overall brand identity. Some examples attached as well. We are looking for someone to work with on future projects as well.

Lyrics are here: https://docs.example.org/document/d/3KTp9wrn_2ZQa8eXb4Lo_fimH7C5m83Jz4Pd70hrtVcA/edit

Music is here: https://audiostream.example.com/suddentides/lantern-road/s-pzkwa

Font styles to use
Sans Serif

Colors

Designer to choose colors to be used in the design.

Requirements
Must have
• Must be consistent with current brand identity and with prior album / single art.

```html
<!DOCTYPE html>
<html lang="en">
<head>
<meta charset="utf-8">
<title>Sudden Tides – Lantern Road single cover</title>
<link rel="stylesheet" href="https://fonts.googleapis.com/css2?family=Jost:wght@300;500&display=swap">
<style>
  :root {
    --paper: #ffffff;
    --sun: #f8ae17;
    --sun-soft: #e9ae30;
    --sage: #9bb07c;
    --tide: #26a9ac;
    --navy: #1c2a58;
    --white: #ffffff;
  }
  html, body {
    margin: 0;
    padding: 0;
    overflow: hidden;
    background: var(--paper);
  }
  .canvas {
    position: relative;
    width: 1200px;
    height: 1192px;
    overflow: hidden;
    background: var(--paper);
  }
  .cover {
    position: absolute;
    left: 170px;
    top: 178px;
    width: 866px;
    height: 865px;
    background: linear-gradient(
      to bottom,
      var(--sun) 0%,
      var(--sun) 45%,
      var(--sun-soft) 65%,
      var(--sage) 82%,
      var(--tide) 96%,
      var(--tide) 100%
    );
  }
  .frame {
    position: absolute;
    left: 0;
    top: 0;
  }
  .single-title {
    position: absolute;
    left: 298px;
    top: 386px;
    margin: 0;
    font-family: "Jost", sans-serif;
    font-weight: 500;
    font-size: 132px;
    line-height: 180px;
    letter-spacing: 2px;
    color: var(--navy);
    text-transform: uppercase;
  }
  .single-title span {
    display: block;
  }
  .dot-rows {
    position: absolute;
    left: 0;
    top: 0;
  }
  .band-name {
    position: absolute;
    right: 206px;
    top: 868px;
    margin: 0;
    font-family: "Jost", sans-serif;
    font-weight: 300;
    font-size: 66px;
    line-height: 72px;
    letter-spacing: 4px;
    color: var(--white);
    text-align: right;
    text-transform: uppercase;
  }
  .band-name span {
    display: block;
  }
</style>
</head>
<body>
<main class="canvas">
  <div class="cover" role="img" aria-label="Chevron stripe pattern in amber and teal, fading to teal at the bottom"></div>

  <svg class="frame" width="1200" height="1192" viewBox="0 0 1200 1192" aria-hidden="true">
    <polyline points="994,936 994,220 211,220 211,1001 714,1001"
              fill="none" stroke="var(--white)" stroke-width="7"/>
  </svg>

  <h1 class="single-title"><span>Lantern</span><span>Road</span></h1>

  <svg class="dot-rows" width="1200" height="1192" viewBox="0 0 1200 1192" aria-hidden="true">
    <g fill="var(--white)">
      <circle cx="312" cy="763" r="7.5"/>
      <circle cx="356" cy="763" r="7.5"/>
      <circle cx="400" cy="763" r="7.5"/>
      <circle cx="444" cy="763" r="7.5"/>
      <circle cx="488" cy="763" r="7.5"/>
      <circle cx="532" cy="763" r="7.5"/>
      <circle cx="576" cy="763" r="7.5"/>
      <circle cx="620" cy="763" r="7.5"/>
      <circle cx="664" cy="763" r="7.5"/>

      <circle cx="443" cy="804" r="7.5"/>
      <circle cx="487" cy="804" r="7.5"/>
      <circle cx="531" cy="804" r="7.5"/>
      <circle cx="576" cy="804" r="7.5"/>
      <circle cx="620" cy="804" r="7.5"/>
      <circle cx="664" cy="804" r="7.5"/>
      <circle cx="708" cy="804" r="7.5"/>
      <circle cx="753" cy="804" r="7.5"/>
      <circle cx="797" cy="804" r="7.5"/>
    </g>
  </svg>

  <p class="band-name"><span>Sudden</span><span>Tides</span></p>
</main>
</body>
</html>
```